Sound Crate Hire (business card/packet folder/stationary)

Designers:
The address will not longer be included in any of these designs. Thanks!

Attention designers,
It was brought to my attention that my brief was too broad and VERY confusing :/. I truly apologize.

This is what I need:
*Front and back business cards.
*A packet folder (front and back) (The size big enough to hold the 8x11 sheets)
I really don't know he size.

*Letter head

I needs to be professional, elegant, and it needs to stand out. Corporate like.

Colors:
Deep Red, Black, Deep blue . Also, follow color scheme of current logo but get creative.

Company: Sound Crate Hire Prairie
Phone: 918.555.0142
Email: Bookings@SoundCrateHirePrairie.example
Web: www.SoundCrateHirePrairie.example (under construction)
Address: 4826 W. 9th Court, Tulsa, OK 74100
Logo: Provided

Project Deadline Extended
Reason: Due to my poor explanation and description of the project, I'm extending the due date of this project.

Target Market(s)

This folder will have my information as a business and it will serve as a marketing material. The audience range age is 18-43.

Industry/Entity Type

Business

Requirements
Must have
• Follow the color scheme provide in the logo.

```html
<!DOCTYPE html>
<html lang="en">
<head>
<meta charset="utf-8">
<title>Sound Crate Hire – Presentation Folder</title>
<link href="https://fonts.googleapis.com/css2?family=Montserrat:wght@400;700&display=swap" rel="stylesheet">
<style>
  :root {
    --stage: #c6c6c6;
    --ink: #060606;
    --panel-light: #1c1c1c;
    --pocket: #0e0e0e;
    --pocket-edge: #2c2c2c;
    --paper: #ffffff;
    --name: #ffffff;
    --accent: #f0642a;
    --muted: #9a9a9a;
    --mark-dark: #2a2a2a;
    --mark-paper: #ececec;
  }
  * { margin: 0; padding: 0; box-sizing: border-box; }
  html, body { width: 1200px; height: 1000px; overflow: hidden; }
  body {
    background: var(--stage);
    font-family: "Montserrat", Arial, sans-serif;
    position: relative;
  }
  .spread {
    position: absolute;
    left: 270px;
    width: 660px;
    height: 440px;
    display: flex;
    box-shadow: 0 10px 24px rgba(0,0,0,.35);
  }
  .spread--outside { top: 30px; }
  .spread--inside { top: 520px; }
  .panel {
    position: relative;
    width: 330px;
    height: 100%;
    overflow: hidden;
    background: radial-gradient(ellipse at 40% 35%, var(--panel-light) 0%, var(--ink) 75%);
  }
  .panel + .panel { border-left: 1px solid #000; }

  /* Faint brand mark used as a large background decoration */
  .backdrop-mark {
    position: absolute;
    display: flex;
    flex-direction: column;
    align-items: center;
    gap: 14px;
  }
  .backdrop-mark__circle {
    width: 170px; height: 170px;
    border-radius: 50%;
    background: var(--mark-dark);
  }
  .backdrop-mark__name {
    color: var(--mark-dark);
    font-weight: 700;
    font-size: 15px;
    letter-spacing: 1px;
    text-transform: uppercase;
    white-space: nowrap;
  }
  .panel--back .backdrop-mark,
  .panel--inner-left .backdrop-mark { left: 50%; top: 55px; transform: translateX(-50%); }

  /* Bold accent disc on the front cover */
  .cover-disc {
    position: absolute;
    top: 40px;
    right: -70px;
    width: 190px; height: 190px;
    border-radius: 50%;
    background: var(--accent);
  }

  .pocket {
    position: absolute;
    left: 0; right: 0; bottom: 0;
    height: 90px;
    background: var(--pocket);
    border-top: 1px solid var(--pocket-edge);
    display: flex;
    align-items: center;
    padding: 0 22px;
    gap: 14px;
  }
  .spread--inside .pocket { height: 120px; }
  .pocket--left { clip-path: polygon(0 0, 62% 0, 86% 24%, 100% 100%, 0 100%); }
  .pocket--right { clip-path: polygon(0 40%, 8% 0, 100% 0, 100% 100%, 0 100%); }
  .spread--inside .pocket--right { padding-top: 30px; }

  .brand { display: flex; align-items: center; gap: 7px; }
  .brand__dot {
    width: 10px; height: 10px;
    border-radius: 50%;
    background: var(--accent);
    flex: none;
  }
  .brand__name {
    color: var(--name);
    font-weight: 700;
    font-size: 13px;
    letter-spacing: .5px;
    text-transform: uppercase;
    white-space: nowrap;
  }
  .brand__name--small { font-size: 9px; }

  .contact {
    list-style: none;
    border-left: 1px solid #444;
    padding-left: 8px;
    font-size: 6px;
    line-height: 9px;
    color: var(--muted);
    white-space: nowrap;
  }
  .contact li::before {
    content: "";
    display: inline-block;
    width: 3px; height: 3px;
    margin-right: 4px;
    vertical-align: middle;
    background: var(--accent);
  }

  .letterhead {
    position: absolute;
    left: 40px;
    top: 120px;
    width: 250px;
    height: 300px;
    background: var(--paper);
    box-shadow: 0 0 4px rgba(0,0,0,.5);
  }
  .letterhead__header {
    height: 36px;
    background: var(--ink);
    display: flex;
    align-items: center;
    justify-content: space-between;
    padding: 0 8px;
    gap: 6px;
  }
  .letterhead__header .brand__name { font-size: 7px; }
  .letterhead__header .brand__dot { width: 7px; height: 7px; }
  .letterhead__header .contact {
    font-size: 4.5px;
    line-height: 7px;
    border-left-color: #333;
    padding-left: 6px;
  }
  .letterhead .backdrop-mark { left: 50%; top: 90px; transform: translateX(-50%); gap: 8px; }
  .letterhead .backdrop-mark__circle { width: 80px; height: 80px; background: var(--mark-paper); }
  .letterhead .backdrop-mark__name { color: var(--mark-paper); font-size: 8px; }
</style>
</head>
<body>

<section class="spread spread--outside" aria-label="Folder outside">
  <div class="panel panel--back">
    <div class="backdrop-mark" aria-hidden="true">
      <span class="backdrop-mark__circle"></span>
      <span class="backdrop-mark__name">Sound Crate Hire</span>
    </div>
    <div class="pocket">
      <div class="brand">
        <span class="brand__dot"></span>
        <span class="brand__name brand__name--small">Sound Crate Hire</span>
      </div>
      <ul class="contact">
        <li>918.555.0142</li>
        <li>918.555.0187</li>
        <li>Bookings@SoundCrateHirePrairie.example</li>
        <li>www.SoundCrateHirePrairie.example</li>
      </ul>
    </div>
  </div>
  <div class="panel panel--front">
    <span class="cover-disc" aria-hidden="true"></span>
    <div class="pocket">
      <div class="brand">
        <span class="brand__dot"></span>
        <span class="brand__name">Sound Crate Hire Prairie</span>
      </div>
    </div>
  </div>
</section>

<section class="spread spread--inside" aria-label="Folder inside">
  <div class="panel panel--inner-left">
    <div class="backdrop-mark" aria-hidden="true">
      <span class="backdrop-mark__circle"></span>
      <span class="backdrop-mark__name">Sound Crate Hire</span>
    </div>
    <div class="pocket pocket--left">
      <div class="brand">
        <span class="brand__dot"></span>
        <span class="brand__name brand__name--small">Sound Crate Hire</span>
      </div>
    </div>
  </div>
  <div class="panel panel--inner-right">
    <article class="letterhead" aria-label="Letterhead">
      <header class="letterhead__header">
        <div class="brand">
          <span class="brand__dot"></span>
          <span class="brand__name">Sound Crate Hire</span>
        </div>
        <ul class="contact">
          <li>918.555.0142</li>
          <li>Bookings@SoundCrateHirePrairie.example</li>
          <li>www.SoundCrateHirePrairie.example</li>
        </ul>
      </header>
      <div class="backdrop-mark" aria-hidden="true">
        <span class="backdrop-mark__circle"></span>
        <span class="backdrop-mark__name">Sound Crate Hire</span>
      </div>
    </article>
    <div class="pocket pocket--right">
      <div class="brand">
        <span class="brand__dot"></span>
        <span class="brand__name">Sound Crate Hire Prairie</span>
      </div>
    </div>
  </div>
</section>

</body>
</html>
```